Bref créative
Brightfield pest control
Stationary business card project for brightfield pest control
Professional
Doug Harlan
4120 w pinecrest ln. meridian idaho 83619
dharlan77@mailvista.net
ALL SERVICES GUARANTEED
Residential.Commercial Service.Certified specialist.Free Estimates
This is the company logo.

```html
<!DOCTYPE html>
<html lang="en">
<head>
<meta charset="utf-8">
<title>Brightfield pest control — Business Card</title>
<link rel="stylesheet" href="https://fonts.googleapis.com/css2?family=PT+Sans:wght@400;700&display=swap">
<style>
  :root {
    --card-white: #ffffff;
    --brand-green: #2aa532;
    --brand-orange: #f7892a;
    --card-edge: #c9c9c9;
    --text-light: #ffffff;
  }
  html, body {
    margin: 0;
    padding: 0;
    overflow: hidden;
    background: var(--card-white);
  }
  .business-card {
    position: relative;
    width: 1200px;
    height: 722px;
    overflow: hidden;
    background: var(--card-white);
    box-sizing: border-box;
    border: 2px solid var(--card-edge);
    font-family: "PT Sans", sans-serif;
  }
  .card-waves {
    position: absolute;
    inset: 0;
  }
  .brand-name {
    position: absolute;
    left: 82px;
    top: 120px;
    display: flex;
    align-items: center;
    gap: 18px;
    color: var(--brand-green);
    font-weight: 700;
    font-size: 50px;
    line-height: 1.02;
  }
  .brand-dot {
    width: 40px;
    height: 40px;
    border-radius: 50%;
    background: var(--brand-green);
    flex: none;
  }
  .guarantee {
    position: absolute;
    right: 78px;
    top: 26px;
    margin: 0;
    color: var(--brand-green);
    font-size: 25px;
    letter-spacing: 0.5px;
  }
  .services {
    position: absolute;
    right: 78px;
    top: 160px;
    margin: 0;
    color: var(--brand-green);
    font-size: 25px;
  }
  .contact-name {
    position: absolute;
    left: 0;
    right: 0;
    top: 336px;
    margin: 0;
    text-align: center;
    color: var(--brand-orange);
    font-weight: 400;
    font-size: 48px;
  }
  .contact-details {
    position: absolute;
    left: 80px;
    top: 528px;
    margin: 0;
    color: var(--text-light);
    font-style: normal;
    font-size: 28px;
    line-height: 40px;
  }
</style>
</head>
<body>
  <main class="business-card">
    <svg class="card-waves" width="1200" height="722" viewBox="0 0 1200 722" aria-hidden="true">
      <path d="M0,440 C420,452 820,430 1200,340 L1200,722 L0,722 Z" fill="var(--brand-green)"/>
      <path d="M0,466 C420,478 820,456 1200,366 L1200,722 L0,722 Z" fill="var(--brand-orange)"/>
    </svg>

    <div class="brand-name">
      <span class="brand-dot"></span>
      <span>brightfield<br>pest control</span>
    </div>

    <p class="guarantee">ALL SERVICES GUARANTEED</p>
    <p class="services">Residential.Commercial Service.Certified specialist.Free Estimates</p>

    <h1 class="contact-name">Doug Harlan</h1>

    <address class="contact-details">
      4120 w pinecrest ln. meridian idaho 83619<br>
      Cell: (208)555-0147<br>
      Email: dharlan77@mailvista.net
    </address>
  </main>
</body>
</html>
```